Packiging of mouse trap

We need a packiging for a new mousetrap called 'Quillnest'. It is a mouse/rat trap. We want to have it pretty simple and modern. The logo of the mouse trap is in the attachment and the measures of the packaging also (don't look at the design, it has nothing to do with us). It's needs to stand out in between the other packaging due to it's simplicity and modern touch.

Font styles to use
Sans Serif

Requirements
Must have
• Simplicity, modern
Should not have
• Too many colors

```html
<!DOCTYPE html>
<html lang="en">
<head>
<meta charset="utf-8">
<title>Quillnest Electronic Rat Trap – Packaging Panels</title>
<link rel="stylesheet" href="https://fonts.googleapis.com/css2?family=Josefin+Sans:wght@600;700&family=Roboto+Condensed:wght@400;700&display=swap">
<style>
  :root {
    --ink: #1c1d1c;
    --paper: #ffffff;
    --panel: #f4f4f2;
    --band: #1f2120;
    --muted: #3a3a3a;
    --fur: #6b5443;
  }
  * { box-sizing: border-box; margin: 0; padding: 0; }
  html, body { width: 1200px; height: 675px; overflow: hidden; background: var(--paper); }
  body { position: relative; font-family: "Josefin Sans", sans-serif; color: var(--ink); }

  .dieline {
    position: absolute;
    top: 57px;
    left: 235px;
    display: flex;
    gap: 18px;
  }
  .panel {
    position: relative;
    height: 560px;
    background: var(--panel);
    overflow: hidden;
    box-shadow: 0 1px 0 rgba(0,0,0,.06), 0 0 0 1px rgba(0,0,0,.05);
  }
  .panel--front { width: 250px; }
  .panel--info { width: 200px; }
  .panel__band {
    position: absolute;
    left: 0; right: 0; bottom: 0;
    height: 76px;
    background: var(--band);
  }

  .product-visual {
    position: absolute;
    border-radius: 14px;
  }
  .product-visual--side {
    top: 24px; left: 58px; width: 118px; height: 290px;
    background: linear-gradient(90deg, #141414 0%, #1d1d1d 70%, #2e2e2e 100%);
    border-radius: 4px 26px 14px 4px;
  }
  .product-visual--top {
    top: 88px; left: 64px; width: 122px; height: 290px;
    background: linear-gradient(90deg, #1a1a1a 0%, #242424 50%, #1a1a1a 100%);
    border-radius: 24px 24px 14px 14px;
  }
  .rodent-visual {
    position: absolute;
    width: 36px; height: 90px;
    border-radius: 18px 18px 6px 6px;
    background: linear-gradient(180deg, var(--fur) 0%, #8a6d57 55%, rgba(200,150,140,.5) 100%);
  }
  .rodent-visual--side { top: 314px; left: 86px; }
  .rodent-visual--top { top: 378px; left: 107px; }

  .wordmark {
    position: absolute;
    left: 0; right: 0;
    text-align: center;
    font-family: "Josefin Sans", sans-serif;
    font-weight: 700;
    font-size: 42px;
    letter-spacing: -1px;
    color: var(--ink);
  }
  .panel--front-a .wordmark { top: 398px; }
  .panel--front-b .wordmark { top: 432px; }

  .descriptor {
    position: absolute;
    left: 0; right: 0;
    text-align: center;
    font-weight: 700;
    font-size: 19px;
    line-height: 20px;
    letter-spacing: 1.5px;
    text-transform: uppercase;
  }
  .panel--front-a .descriptor { top: 440px; font-size: 16px; line-height: 18px; top: 446px; }
  .panel--front-b .descriptor { top: 20px; font-size: 22px; line-height: 23px; }

  .info {
    padding: 14px 14px 0;
    font-family: "Roboto Condensed", sans-serif;
    font-size: 6.6px;
    line-height: 1.45;
    color: var(--muted);
  }
  .info h3 {
    font-size: 7px;
    font-weight: 700;
    text-transform: uppercase;
    color: var(--ink);
    margin-top: 6px;
  }
  .info h3:first-child { margin-top: 0; }
  .info .note { font-style: italic; margin-top: 6px; }
  .info .warning { margin-top: 18px; }
  .info .warning h3 { margin-bottom: 4px; }

  .legal {
    position: absolute;
    left: 14px; bottom: 96px;
    font-family: "Roboto Condensed", sans-serif;
    font-size: 6.4px;
    line-height: 1.4;
    color: var(--muted);
  }
  .legal strong { color: var(--ink); text-transform: uppercase; }
</style>
</head>
<body>
<main class="dieline">

  <section class="panel panel--front panel--front-a">
    <div class="product-visual product-visual--side" role="img" aria-label="Black electronic trap unit seen from the side"></div>
    <div class="rodent-visual rodent-visual--side" role="img" aria-label="Photo of a rat entering the trap tunnel, seen from behind"></div>
    <div class="wordmark">Quillnest</div>
    <div class="descriptor">Electronic<br>Rat Trap</div>
    <div class="panel__band"></div>
  </section>

  <section class="panel panel--front panel--front-b">
    <div class="descriptor">Electronic<br>Rat Trap</div>
    <div class="product-visual product-visual--top" role="img" aria-label="Black electronic trap unit seen from above with lid switch"></div>
    <div class="rodent-visual rodent-visual--top" role="img" aria-label="Photo of a rat entering the trap tunnel, seen from above"></div>
    <div class="wordmark">Quillnest</div>
    <div class="panel__band"></div>
  </section>

  <section class="panel panel--info">
    <div class="info">
      <h3>4 C batteries eliminate up to 60 rats</h3>
      <h3>Quick &amp; humane</h3>
      <p>Humanely removes up to 60 rodents</p>
      <h3>Smart rodent detection</h3>
      <p>Built-in safety sensors to protect kids and pets</p>
      <h3>Easy cleanups</h3>
      <p>No-touch, no-see, no-mess disposal</p>
      <h3>New &amp; improved design</h3>
      <p>Efficient zap system with no-escape tunnel design</p>
      <p class="note">Each trap requires 4 C batteries (batteries not included)</p>

      <div class="warning">
        <h3>Warning</h3>
        <p>Electric shock and spark hazards.</p>
        <p>Ignition: Use indoors on dry, clean surfaces. Do not use near flammable vapors, liquids or solids, or in barns, stables or dusty locations.</p>
        <p>High voltage: Keep out of reach of children and pets. Handle only with dry hands or rubber gloves. Turn off the power before placing bait. Do not touch the metal plate when the device is on.</p>
        <p>Electromagnetic waves: Keep pacemakers and other life-sustaining equipment at least one foot away. Failure to follow all precautions may result in electric shock, fire or serious injury.</p>
      </div>

      <div class="warning">
        <h3>Warning</h3>
        <p>This product may expose you to lead compounds known to cause cancer and birth defects. For details visit labelnotice.example.org.</p>
      </div>
    </div>

    <div class="legal">
      <strong>Fernmoor</strong><br>
      Electronic Rat Trap &nbsp; Model No.: QN220<br>
      U.S. Pat. 00000000 and other pending patents<br>
      www.fernmoorhome.com<br>
      Design in USA<br>
      Made in China
    </div>
    <div class="panel__band"></div>
  </section>

</main>
</body>
</html>
```